Varemo Group Business Card Design

The CEO is looking for a new trendy look for his business card.
You can stay with current branding or come up with something new/creative. It can be 3D, including Medical Office buildings. You can use our logo in a variety of colors. Please include name, title, company name, company website, email address, cell number

Target Market(s)

Real Estate Development and Construction

Industry/Entity Type

Health care real estate

Contact Information for Business Card

Rohesh Kumbar, CEO M-727.418.9062 E-roheshkumbar@varemo.com Address:4100 Lindell Ave, Tampa, FL 33611 www.varemo.com

Font styles to use
Other font styles liked:
• Be creative

Requirements
Must have
• Creative, trendy look
Nice to have
• Please go to our website to get a feel- www. varemo.com
Should not have
• small fonts

```html
<!DOCTYPE html>
<html lang="en">
<head>
<meta charset="utf-8">
<title>Varemo Group – Business Card Concept</title>
<link rel="stylesheet" href="https://fonts.googleapis.com/css2?family=Montserrat:wght@500;600;700;800&family=Open+Sans:wght@400;700&display=swap">
<style>
  :root {
    --stage: #5e2622;
    --card-red: #c14b56;
    --card-red-deep: #a8323f;
    --navy: #3d4577;
    --paper: #ececec;
    --brand-red: #b3202f;
    --ink: #1a1a1a;
    --white: #ffffff;
    --tint: #e7c9cc;
  }
  * { box-sizing: border-box; margin: 0; padding: 0; }
  html, body { width: 1200px; height: 2289px; overflow: hidden; }
  body { background: var(--white); font-family: "Open Sans", sans-serif; color: var(--ink); }

  .stage {
    height: 1490px; background: var(--stage);
    display: grid; grid-template-columns: 330px 330px; grid-template-rows: 578px 578px;
    gap: 60px; justify-content: center; align-content: center;
  }
  .card { position: relative; overflow: hidden; font-family: "Montserrat", sans-serif; box-shadow: 0 18px 40px rgba(0,0,0,.35); }
  .card--red { background: var(--card-red); color: var(--white); }
  .card--deep { background: var(--card-red-deep); color: var(--white); }
  .card--paper { background: var(--paper); color: var(--navy); }

  .card__shapes { position: absolute; inset: 0; width: 100%; height: 100%; }
  .card__name { position: absolute; left: 34px; top: 92px; font-size: 34px; font-weight: 800; line-height: 1.05; }
  .card__title { font-size: 16px; font-weight: 500; margin-left: 8px; }
  .card__contacts { position: absolute; left: 34px; top: 240px; list-style: none; font-size: 13px; font-weight: 500; line-height: 1.5; }
  .card__contacts li { display: flex; gap: 10px; align-items: flex-start; margin-bottom: 4px; }
  .card__contacts svg { flex: none; width: 14px; height: 14px; margin-top: 3px; }
  .card__web { position: absolute; left: 0; right: 0; bottom: 46px; text-align: center; font-size: 14px; font-weight: 700; }

  .card--paper .card__name { left: 120px; top: 60px; font-size: 30px; }
  .card--paper .card__contacts { left: 120px; top: 190px; font-size: 12px; }
  .card--paper .card__web { left: 120px; bottom: 170px; text-align: left; font-size: 13px; }

  .card__brand { position: absolute; inset: 0; display: flex; align-items: center; justify-content: center; font-size: 34px; font-weight: 800; color: var(--white); }

  .card__motif { position: absolute; background: var(--tint); opacity: .7; }

  .brief { padding: 80px 44px 0; }
  .brief__heading { text-align: center; font-size: 27px; font-weight: 700; margin-bottom: 48px; }
  .brief__text { font-size: 25px; line-height: 1.38; }

  .concepts { display: flex; justify-content: space-between; padding: 84px 110px 0; }
  .concept { width: 320px; }
  .concept__label { color: var(--brand-red); font-family: "Montserrat", sans-serif; font-weight: 700; font-size: 24px; margin-bottom: 30px; }
  .concept__brand { display: flex; align-items: center; gap: 10px; font-family: "Montserrat", sans-serif; font-weight: 800; font-size: 38px; color: var(--ink); margin: 0 0 40px 20px; white-space: nowrap; }
  .concept__brand i { width: 16px; height: 16px; background: var(--brand-red); }
  .concept--two .concept__brand { color: var(--brand-red); }
  .concept__items { display: flex; gap: 50px; align-items: flex-end; }
  .concept__item { text-align: center; font-size: 15px; font-weight: 700; }
  .concept__swatch { width: 110px; height: 110px; margin: 0 auto 14px; }
  .swatch--small { width: 50px; height: 50px; margin-bottom: 34px; background: #d9a3a9; }
  .swatch--navy { background: #dfe2ee; }
  .swatch--pale { background: #e6e6e6; }
  .swatch--tint { background: #f0cfd3; }
</style>
</head>
<body>
  <section class="stage">
    <article class="card card--red">
      <svg class="card__shapes" viewBox="0 0 330 578" aria-hidden="true">
        <path d="M110 0 H330 V20 C260 60 170 70 110 0 Z" fill="var(--navy)"/>
        <path d="M0 120 C40 140 60 190 0 220 Z" fill="var(--navy)"/>
        <path d="M120 380 H270 A40 40 0 0 1 270 460 H120 A40 40 0 0 1 120 380 Z" fill="var(--navy)"/>
        <path d="M0 440 C60 470 80 520 40 578 H0 Z" fill="var(--navy)"/>
      </svg>
      <h2 class="card__name">Rohesh<br>Kumbar<span class="card__title">CEO</span></h2>
      <ul class="card__contacts">
        <li><svg viewBox="0 0 14 14" aria-label="Phone"><rect x="3.5" y="0.5" width="7" height="13" rx="1.5" fill="none" stroke="#fff" stroke-width="1.4"/><circle cx="7" cy="11" r="0.9" fill="#fff"/></svg>727.418.9062</li>
        <li><svg viewBox="0 0 14 14" aria-label="Email"><rect x="0.7" y="2.7" width="12.6" height="8.6" fill="none" stroke="#fff" stroke-width="1.4"/><path d="M1 3l6 5 6-5" fill="none" stroke="#fff" stroke-width="1.4"/></svg>roheshkumbar@varemo.com</li>
        <li><svg viewBox="0 0 14 14" aria-label="Address"><path d="M7 13.5C3.5 9 2.5 7.3 2.5 5a4.5 4.5 0 0 1 9 0c0 2.3-1 4-4.5 8.5z" fill="#fff"/><circle cx="7" cy="5" r="1.6" fill="var(--card-red)"/></svg>4100 Lindell Ave, Tampa,<br>FL 33611</li>
      </ul>
      <p class="card__web">www.varemo.com</p>
    </article>

    <article class="card card--red">
      <p class="card__brand">Varemo Group</p>
    </article>

    <article class="card card--deep">
      <p class="card__brand">Varemo Group</p>
    </article>

    <article class="card card--paper">
      <div class="card__motif" role="img" aria-label="Large outlined letterform decoration" style="left:0;top:0;width:90px;height:170px;"></div>
      <div class="card__motif" role="img" aria-label="Large outlined letterform decoration" style="left:0;bottom:0;width:330px;height:130px;"></div>
      <h2 class="card__name">Rohesh<br>Kumbar<span class="card__title">CEO</span></h2>
      <ul class="card__contacts">
        <li><svg viewBox="0 0 14 14" aria-label="Phone"><rect x="3.5" y="0.5" width="7" height="13" rx="1.5" fill="none" stroke="var(--brand-red)" stroke-width="1.4"/><circle cx="7" cy="11" r="0.9" fill="var(--brand-red)"/></svg>727.418.9062</li>
        <li><svg viewBox="0 0 14 14" aria-label="Email"><rect x="0.7" y="2.7" width="12.6" height="8.6" fill="none" stroke="var(--brand-red)" stroke-width="1.4"/><path d="M1 3l6 5 6-5" fill="none" stroke="var(--brand-red)" stroke-width="1.4"/></svg>roheshkumbar@varemo.com</li>
        <li><svg viewBox="0 0 14 14" aria-label="Address"><path d="M7 13.5C3.5 9 2.5 7.3 2.5 5a4.5 4.5 0 0 1 9 0c0 2.3-1 4-4.5 8.5z" fill="var(--brand-red)"/><circle cx="7" cy="5" r="1.6" fill="var(--paper)"/></svg>4100 Lindell Ave, Tampa,<br>FL 33611</li>
      </ul>
      <p class="card__web">www.varemo.com</p>
    </article>
  </section>

  <section class="brief">
    <h1 class="brief__heading">Business Card Concept</h1>
    <p class="brief__text">In addition to the unique horizontal layout , the design merges abstract geometric shapes with the essence of the logo's core concept, crafting a harmonious visual identity. Inspired by the logo's inherent dynamics and aesthetics, the design employs clean lines, bold forms, and calculated symmetry to convey innovation, precision, and creativity.</p>
  </section>

  <section class="concepts">
    <div class="concept concept--one">
      <h3 class="concept__label">CONCEPT 1</h3>
      <p class="concept__brand"><i></i>Varemo Group</p>
      <div class="concept__items">
        <div class="concept__item"><div class="concept__swatch swatch--small" role="img" aria-label="Brand icon area"></div>Icon</div>
        <div class="concept__item"><div class="concept__swatch swatch--navy" role="img" aria-label="Line pattern built from the brand icon"></div>Pattern</div>
      </div>
    </div>
    <div class="concept concept--two">
      <h3 class="concept__label">CONCEPT 2</h3>
      <p class="concept__brand">Varemo Group</p>
      <div class="concept__items">
        <div class="concept__item"><div class="concept__swatch swatch--pale" role="img" aria-label="Brand icon area"></div>Icon</div>
        <div class="concept__item"><div class="concept__swatch swatch--tint" role="img" aria-label="Outlined letterform pattern"></div>Pattern</div>
      </div>
    </div>
  </section>
</body>
</html>
```